zVerda Corporate Website

zVerda is a well-funded start up developing an Online Marketing Platform for small businesses in Europe.
We are launching in February 2012 with all-in-one online marketing services including professional website, DIY SEO, Dashboard with Reports and Online marketing tools, and Support.
Our internal web designer has come up with a preliminary website design which we wish to continue to improve using new ideas, colours, layout, image, etc.
The brief is very simple - improve the website whether it is look & feel, ease of use, conversion rate - we are looking for overall improvements.
The contest will last 5 days and we will award the winner £300.
If you are the winner , you will also be required to provide designs for 3 more internal pages adhering to the proposed home page design.
Judging criteria : -
Visual Design
Layout must adhere to best practices and wire frame. If you decide to move elements around significantly please provide reason
Functional, informative and drives calls to action
Industry/Entity Type
Marketing
Look and feel
Each slider illustrates characteristics of the customer's brand and the style your logo design should communicate.

```html
<!DOCTYPE html>
<html lang="en">
<head>
<meta charset="utf-8">
<title>zVerda – Online Marketing for Small Business</title>
<link href="https://fonts.googleapis.com/css2?family=Arimo:ital,wght@0,400;0,700;1,400;1,700&display=swap" rel="stylesheet">
<style>
:root{
  --navy-dark:#081f4c;
  --navy:#123a78;
  --navy-light:#1d4b8f;
  --orange:#f7941d;
  --orange-deep:#e8660c;
  --band:#fdbd5a;
  --green:#6fb03f;
  --text:#333;
  --muted:#666;
  --rule:#d8d8d8;
  --red:#c0141c;
  --black:#1b1b1b;
  --footer:#e0eef8;
  --footer-panel:#cde3f3;
  --link:#1b4a7c;
  --blue-frame:#1a8ad4;
}
*{box-sizing:border-box;margin:0;padding:0}
html,body{width:977px;height:1200px;overflow:hidden}
body{position:relative;background:#fff;font-family:"Arimo",Arial,sans-serif;color:var(--text)}
.abs{position:absolute}
svg{display:block}

/* header */
.site-header{left:0;top:0;width:977px;height:48px;background:linear-gradient(#0e2e68,var(--navy-dark))}
.brand{left:147px;top:9px;display:flex;align-items:center;gap:7px;color:#fff;font-size:27px}
.brand-dot{width:24px;height:24px;border-radius:50%;background:var(--orange)}
.main-nav a{position:absolute;top:14px;height:20px;line-height:20px;font-size:10px;color:#fff;text-decoration:none;letter-spacing:.2px}
.main-nav .current{background:#1f4a8a;color:var(--orange);padding:0 9px;border-radius:2px}
.login{left:726px;top:0;width:104px;height:48px;background:var(--navy-light);color:#fff;font-size:10px;display:flex;align-items:center;justify-content:center;gap:10px}
.login-key{width:22px;height:22px;border-radius:50%;background:var(--orange);display:flex;align-items:center;justify-content:center}

/* hero */
.benefits{left:147px;top:73px;list-style:none}
.benefits li{display:flex;align-items:center;gap:7px;height:25px;color:var(--green);font-size:13px}
.tick{width:11px;height:11px;border:1px solid #aaa;border-radius:50%;display:flex;align-items:center;justify-content:center}
.tagline{left:147px;top:196px;width:220px;font-size:12.5px;line-height:16px;color:#444}
.signup{left:147px;top:238px;width:102px;height:38px;border-radius:4px;background:linear-gradient(#2a66c4,#0d3990);color:#fff;text-align:center;border:1px solid #0a2c70}
.signup small{display:block;font-size:8.5px;font-weight:700;margin-top:6px}
.signup strong{display:block;font-size:15px;line-height:16px}
.hero-art{left:370px;top:55px;width:460px;height:260px;background:radial-gradient(ellipse at 55% 60%,#dfeaf6 0%,#f4f8fc 55%,#fff 80%)}
.slide-arrows{left:785px;top:280px;display:flex;gap:4px}
.slide-arrows span{width:20px;height:20px;background:#cfcfcf;color:#fff;font-size:12px;text-align:center;line-height:20px}
.promo-fold{left:147px;top:304px;width:0;height:0;border-left:10px solid var(--band);border-top:12px solid transparent;filter:brightness(.85)}
.promo-band{left:147px;top:316px;width:683px;height:48px;background:var(--band);text-align:center;overflow:hidden}
.promo-band h1{color:#fff;font-size:16px;line-height:20px;font-style:italic;font-weight:700;margin-top:7px;letter-spacing:-.3px;white-space:nowrap}
.promo-band p{color:#3c3c3c;font-size:12px;line-height:15px;margin-top:1px;white-space:nowrap}

/* features */
.features{left:0;top:378px;width:977px;height:106px;background:linear-gradient(#fafafa,#e3e3e3);border-top:1px solid var(--rule);border-bottom:1px solid var(--rule)}
.feature{position:absolute;top:8px;width:150px;text-align:center}
.feature-icon{display:block;width:40px;height:40px;margin:0 auto}
.feature h2{font-size:12.5px;line-height:15px;font-weight:700;color:#111;margin-top:8px}
.feature p{font-size:9.5px;color:var(--muted);line-height:11px;margin-top:8px}

/* pricing */
.plan{top:505px;width:160px;height:125px;border:1px solid #e2e2e2;background:linear-gradient(#fafafa 30%,#e6e6e6);box-shadow:0 2px 2px rgba(0,0,0,.12)}
.ribbon{position:absolute;left:6px;top:-1px;width:32px;height:132px}
.seal{position:absolute;left:-1px;top:20px;width:56px;height:56px;border-radius:50%;border:4px dotted;display:flex;flex-direction:column;align-items:center;justify-content:center;color:#fff;font-size:15px;line-height:15px}
.seal em{font-style:normal;font-size:6px;color:#ffd23d;font-weight:700}
.plan h3{position:absolute;left:57px;top:14px;font-size:14px;line-height:16px;font-weight:700;color:#111}
.plan .offer{position:absolute;left:60px;top:67px;font-size:9px;color:#222}
.plan .tag{position:absolute;right:0;top:96px;height:17px;line-height:17px;padding:0 7px;color:#fff;font-size:8.5px;font-weight:700;white-space:nowrap}
.how{left:668px;top:505px;width:162px;height:124px;border:1px solid #d9d9d9;background:#fff}
.how h4{height:26px;line-height:26px;padding-left:8px;font-size:10.5px;color:var(--navy);background:linear-gradient(#fafafa,#e4e4e4)}
.how p{font-size:9px;line-height:12.5px;color:#333;padding:9px 12px 0 9px}
.how a{position:absolute;right:8px;bottom:7px;font-size:9px;color:var(--orange-deep);text-decoration:none}

/* examples */
.examples-bar{left:147px;top:659px;width:683px;height:27px;background:#f0f0f0}
.examples-bar h2{font-size:13px;color:var(--orange-deep);font-weight:700;line-height:27px;padding-left:7px}
.examples-bar .nav{position:absolute;right:8px;top:8px;display:flex;gap:2px}
.examples-bar .nav span{width:11px;height:11px;background:#999;color:#fff;font-size:8px;line-height:11px;text-align:center}
.example{top:706px;width:325px;height:150px}
.screen{position:absolute;left:0;top:0;width:142px;height:120px;background:linear-gradient(#222 0,#222 78%,#c8c8c8 78%,#e4e4e4 100%);border-radius:3px}
.screen::before{content:"";position:absolute;left:6px;top:6px;width:130px;height:83px;background:linear-gradient(#f5f8fb,#d7e4f0)}
.quote{position:absolute;left:168px;top:0;width:160px;font-size:9.5px;line-height:14px;color:#666}
.quote p+p{margin-top:14px}
.quote cite{position:absolute;right:4px;top:112px;font-size:9px;color:var(--orange-deep);font-style:italic;white-space:nowrap}
.visit{position:absolute;left:0;top:126px;font-size:8.5px;line-height:12px;color:#777;font-style:italic}

/* footer */
.site-footer{left:0;top:895px;width:977px;height:305px;background:var(--footer)}
.footer-panel{left:153px;top:895px;width:670px;height:120px;background:var(--footer-panel)}
.footer-col{top:916px;font-size:8.5px;color:var(--link)}
.footer-col h5{font-size:8.5px;font-weight:700;color:#111;margin-left:13px;margin-bottom:9px}
.footer-col ul{list-style:none;border-left:1px solid #8fb6d6;padding-left:13px}
.footer-col li{line-height:12.5px}
.newsletter{left:625px;top:916px;width:180px;height:74px;border:2px solid var(--blue-frame);background:var(--footer-panel)}
.newsletter h5{position:absolute;left:-2px;top:-3px;padding:0 4px 0 2px;background:var(--footer-panel);font-size:10.5px;font-weight:400;color:#111}
.newsletter .email{position:absolute;left:9px;top:22px;width:105px;height:20px;background:#fff;border:1px solid #bbb;font-size:8px;color:#999;font-style:italic;line-height:18px;padding-left:6px}
.newsletter .submit{position:absolute;left:118px;top:22px;width:46px;height:19px;background:linear-gradient(#ffb23e,var(--orange-deep));color:#fff;font-size:8.5px;font-weight:700;text-align:center;line-height:19px;border-radius:2px}
.newsletter .share{position:absolute;left:10px;top:50px;height:13px;padding:0 5px;border:1px solid #aaa;border-radius:2px;background:#f5f5f5;font-size:8px;line-height:11px;color:#333}
.newsletter .friend{position:absolute;left:68px;top:49px;display:flex;align-items:center;gap:6px;font-size:8.5px;color:var(--link)}
.sq{display:inline-block;width:13px;height:13px;background:var(--navy-light)}
.footer-copy{left:147px;top:1027px;width:683px;text-align:center;font-size:8.5px;line-height:12.5px;color:#555}
.footer-copy p+p{margin-top:12px}
.footer-rule{left:147px;top:1165px;width:683px;height:1px;background:#b9cfe0}
.copyright{left:147px;top:1178px;font-size:8.5px;color:#555}
.footer-social{left:803px;top:1174px;display:flex;gap:2px}
</style>
</head>
<body>

<header class="site-header abs">
  <div class="brand abs"><span class="brand-dot"></span>zVerda</div>
  <nav class="main-nav">
    <a class="current" style="left:370px">HOME</a>
    <a style="left:430px">QUICK TOUR</a>
    <a style="left:510px">PRICING</a>
    <a style="left:571px">ABOUT US</a>
    <a style="left:642px">CONTACT US</a>
  </nav>
  <div class="login abs">LOGIN
    <span class="login-key"><svg width="8" height="11" viewBox="0 0 8 11"><circle cx="4" cy="3.5" r="3" fill="#fff"/><rect x="2.5" y="5" width="3" height="6" fill="#fff"/></svg></span>
  </div>
</header>

<ul class="benefits abs">
  <li><span class="tick"><svg width="7" height="6" viewBox="0 0 7 6"><path d="M1 3l2 2 3-4" stroke="#999" fill="none"/></svg></span>BUSINESS WEBSITE</li>
  <li><span class="tick"><svg width="7" height="6" viewBox="0 0 7 6"><path d="M1 3l2 2 3-4" stroke="#999" fill="none"/></svg></span>ONLINE MARKETING</li>
  <li><span class="tick"><svg width="7" height="6" viewBox="0 0 7 6"><path d="M1 3l2 2 3-4" stroke="#999" fill="none"/></svg></span>DASHBOARD CONTROLS</li>
  <li><span class="tick"><svg width="7" height="6" viewBox="0 0 7 6"><path d="M1 3l2 2 3-4" stroke="#999" fill="none"/></svg></span>FULL SETUP &amp; SUPPORT</li>
</ul>
<p class="tagline abs">GETTING A WEBSITE HAS NEVER<br>BEEN SO SIMPLE</p>
<a class="signup abs"><small>SIGN UP NOW FOR</small><strong>FREE!</strong></a>

<div class="hero-art abs" role="img" aria-label="Illustration of a puzzled businessman surrounded by speech bubbles asking about SEO, blogs, social media, banners and other marketing questions"></div>
<div class="slide-arrows abs"><span>&#8592;</span><span>&#8594;</span></div>

<div class="promo-fold abs"></div>
<section class="promo-band abs">
  <h1>THE COMPLETE ONLINE MARKETING SOLUTION FOR SMALL BUSINESS WEBSITES</h1>
  <p>“Get a big online presence and more sales leads in 30 minutes”</p>
</section>

<section class="features abs">
  <div class="feature" style="left:152px">
    <svg class="feature-icon" viewBox="0 0 40 40" role="img" aria-label="Bar chart icon"><rect x="2" y="4" width="10" height="34" fill="#5cb630"/><rect x="14" y="22" width="10" height="16" fill="#d9262b"/><rect x="26" y="12" width="10" height="26" fill="#f5a11a"/></svg>
    <h2>CASE STUDIES</h2><p>Read real stories about small business online...</p>
  </div>
  <div class="feature" style="left:324px">
    <div class="feature-icon" role="img" aria-label="Light bulb icon" style="background:radial-gradient(circle at 50% 40%,#ffe35a 0 45%,transparent 47%)"></div>
    <h2>HOW TO</h2><p>Learn from our online marketin tips for small business...</p>
  </div>
  <div class="feature" style="left:498px">
    <div class="feature-icon" role="img" aria-label="Chat bubbles icon" style="background:radial-gradient(ellipse at 60% 35%,#4fb3e6 0 30%,transparent 32%),radial-gradient(ellipse at 38% 62%,#63c04a 0 30%,transparent 32%)"></div>
    <h2>NEWS &amp; CHATTER</h2><p>Get up to-date news &amp; chatter about online marketing...</p>
  </div>
  <div class="feature" style="left:674px">
    <div class="feature-icon" role="img" aria-label="Presenter with clock icon" style="background:radial-gradient(circle at 40% 50%,#3a3a3a 0 35%,transparent 37%),radial-gradient(circle at 72% 62%,#a9c9e6 0 22%,transparent 24%)"></div>
    <h2>DEMO</h2><p>Find out what zVerda can do for your business...</p>
  </div>
</section>

<article class="plan abs" style="left:147px">
  <div class="ribbon" style="background:var(--red)"></div>
  <div class="seal" style="background:var(--red);border-color:var(--red)">£ 199<em>VALUE</em></div>
  <h3>FREE SET UP</h3><span class="offer">WEB OFFER ONLY</span>
  <span class="tag" style="background:var(--red)">FREE</span>
</article>
<article class="plan abs" style="left:321px">
  <div class="ribbon" style="background:var(--navy)"></div>
  <div class="seal" style="background:var(--navy);border-color:var(--navy)">£ 22<em>VALUE</em></div>
  <h3>BIG ONLINE<br>PRESENCE</h3><span class="offer" style="top:58px;line-height:12px">BUSINESS WEBSITE<br>&amp; EASY DASHBOARD</span>
  <span class="tag" style="background:var(--navy)">PRO PACKAGE</span>
</article>
<article class="plan abs" style="left:495px">
  <div class="ribbon" style="background:var(--black)"></div>
  <div class="seal" style="background:var(--black);border-color:var(--black)">£ 29<em>VALUE</em></div>
  <h3>MORE SALES<br>LEADS</h3><span class="offer">WEB OFFER ONLY</span>
  <span class="tag" style="background:var(--black)">TURBO SALES PRO PLUS</span>
</article>
<aside class="how abs">
  <h4>HOW DOES IT WORKS?</h4>
  <p>Lorem Ipsum is simply dummy text of the printing and industry. Lorem Ipsum has been the industry's standard dummy text ever since the 1500s</p>
  <a>Read More &#9656;</a>
</aside>

<div class="examples-bar abs">
  <h2>VIEW EXAMPLES OF OUR STUNNING BUSINESS WEBSITES</h2>
  <div class="nav"><span>&#9666;</span><span>&#9656;</span></div>
</div>

<div class="example abs" style="left:147px">
  <div class="screen" role="img" aria-label="Desktop monitor showing a sample business website"></div>
  <div class="quote">
    <p>Lorem Ipsum is simply dummy text of the typesetting industry.</p>
    <p>Lorem Ipsum has been. The industry's standard dummy text ever since the 1500s, when an unknown printer took a galley of type.</p>
    <cite>-Lorem Ipsum Text</cite>
  </div>
  <p class="visit">Visit Website:<br>http://www.zverda.com/</p>
</div>
<div class="example abs" style="left:506px">
  <div class="screen" role="img" aria-label="Desktop monitor showing a sample business website"></div>
  <div class="quote">
    <p>Lorem Ipsum is simply dummy text of the typesetting industry.</p>
    <p>Lorem Ipsum has been. The industry's standard dummy text ever since the 1500s, when an unknown printer took a galley of type.</p>
    <cite>-Lorem Ipsum Text</cite>
  </div>
  <p class="visit">Visit Website:<br>http://www.zverda.com/</p>
</div>

<footer>
  <div class="site-footer abs"></div>
  <div class="footer-panel abs"></div>
  <div class="footer-col abs" style="left:172px">
    <h5>COMPANY</h5>
    <ul><li>Search Marketing -<br>Organic / Natural (SEO)</li><li>Social Media</li><li>Web Anaytics</li></ul>
  </div>
  <div class="footer-col abs" style="left:328px">
    <h5>CUSTOMER SERVICES</h5>
    <ul><li>Contact Us</li><li>Customer Support</li><li>Request a Call Back</li><li>FAQ's</li></ul>
  </div>
  <div class="footer-col abs" style="left:496px">
    <h5>INFORMATION</h5>
    <ul><li>Site Map</li><li>Terms &amp; Conditions</li><li>&nbsp;</li><li>&nbsp;</li></ul>
  </div>
  <div class="newsletter abs">
    <h5>Subscribe for Newsletter</h5>
    <div class="email">Your Email</div>
    <div class="submit">SUBMIT</div>
    <span class="share">Chirp</span>
    <span class="friend"><span class="sq"></span>Become a Friend</span>
  </div>
  <div class="footer-copy abs">
    <p>zVerda will build your business website, optimise SEP marketing and make recommendations on best practies to help you win customers. Let our team of experts design a business website for you. Choose a business website from zVerda"s broad array of fabulous, customisable business websites and our experts will have your business onlune minutes. zVerda lets you create a professional business website without the need to know how to code or programme.</p>
    <p>Your business website comes with automatic Internet marketing, marketing on the Interned is easy with zVerda, we automatically optimise your site for SEO marketing and we can Searchly ad campaigns when you need them. Get a business website with online marketing not. zVerda brings your Small Business Website to LIFE!</p>
    <p>View our example business websites above, watch the video demo to see how to make a business website or call us now and get your business marketing online today. The zVerda website builder gives you a professional online appearance - post your own images, give customers your latest news and create customer testimonials, it's the most complete online marketing solution for your business.</p>
  </div>
  <div class="footer-rule abs"></div>
  <p class="copyright abs">© 2012 zVerda Pvt. Ltd. All Rights Reserved.</p>
  <div class="footer-social abs"><span class="sq" style="width:12px;height:12px"></span><span class="sq" style="width:12px;height:12px;background:#3fa9e0"></span></div>
</footer>

</body>
</html>
```